Dentist logo, business card and website

I have done an amateur job of creating a logo, business card and website. I would like it to look more professional. the current website can be found at www.dorenkamsel.com - I would like the website to be built and run through wix.com. The content on the website is as I would like it but I am open to suggestions.

The logo should be simple, may be best to keep to the letter DK - maybe to look like the V is a reflection of the A? Again, I am open to suggestions (I have attached a couple of images I have used on presentations but I would like the logo that you design to have a 'no fill' background so it can be placed on slides (for presentations etc).

The colour scheme seems wrong for a dentist, perhaps duck egg with black writing would be better? This applies to the business card as well (I have attached a PDF of some I have had made in the past but again they look amateur and colour scheme is wrong. The business cards should be landscape, have the logo in the top right corner, my name and qualifications in the middle, and my website and physical address in the bottom left corner: Glanmorfa Dental Surgery, 41-43 Ffordd y Bont, Cardiff CF23 9RT.

Target Market(s)

30-60 year olds

Industry/Entity Type

Dental

Contact Information for Business Card

Please see brief and uploads.

Logo Text

DK

Number of Pages Required

4 page

Font styles to use
Decorative
Script

Requirements
Must have
• A sophisticated mature feel.
Nice to have
• Simplicity.
Should not have
• Anything too complicated.

```html
<!DOCTYPE html>
<html lang="en">
<head>
<meta charset="utf-8">
<title>Doren Kamsel – About Me</title>
<link rel="stylesheet" href="https://fonts.googleapis.com/css2?family=Cinzel:wght@700&family=EB+Garamond:wght@400&family=Open+Sans:wght@400&display=swap">
<style>
  :root {
    --nav-bg: #eceeee;
    --nav-active: #a6c9d1;
    --nav-text: #3c3f41;
    --hero-panel: #a6c9d1;
    --hero-bg: #e9ebeb;
    --portrait-light: #c9b3a4;
    --portrait-dark: #4f6283;
    --body-bg: #d2e3e7;
    --rule: #eef5f7;
    --ink: #111;
    --text: #333a3d;
    --accent: #1a72cf;
    --social-a: #3b54a8;
    --social-b: #2a9be8;
  }
  * { box-sizing: border-box; margin: 0; padding: 0; }
  html, body { width: 1166px; height: 1200px; overflow: hidden; background: var(--body-bg); }
  .page { position: relative; width: 1166px; height: 1200px; overflow: hidden; font-family: "Open Sans", sans-serif; color: var(--text); }

  .site-nav { position: absolute; top: 0; left: 0; width: 1166px; height: 59px; background: var(--nav-bg); border-bottom: 1px solid #dfe3e4; }
  .nav-list { list-style: none; position: absolute; left: 258px; top: 0; height: 59px; display: flex; }
  .nav-item { height: 59px; display: flex; align-items: center; gap: 6px; padding: 0 12px; font-size: 14px; letter-spacing: 0.3px; color: var(--nav-text); text-transform: uppercase; }
  .nav-item.is-active { background: var(--nav-active); padding: 0 18px; }
  .nav-item svg { width: 11px; height: 12px; }
  .menu-toggle { position: absolute; left: 1005px; top: 22px; font-size: 13px; letter-spacing: 2px; color: var(--nav-text); display: flex; align-items: center; gap: 4px; }

  .hero { position: absolute; top: 67px; left: 0; width: 1166px; height: 474px; background: var(--hero-bg); }
  .hero-shape { position: absolute; inset: 0; }
  .hero-name { position: absolute; left: 164px; top: 92px; font-family: "Cinzel", serif; font-weight: 700; font-size: 40px; color: var(--ink); letter-spacing: 0.5px; line-height: 1; white-space: nowrap; }
  .hero-quals { position: absolute; left: 189px; top: 143px; font-family: "Open Sans", sans-serif; font-size: 17px; color: var(--ink); white-space: nowrap; }
  .contact-list { list-style: none; position: absolute; left: 168px; top: 189px; font-family: "EB Garamond", serif; font-size: 19px; color: var(--ink); line-height: 27px; }
  .contact-list li { display: flex; gap: 9px; }
  .contact-list svg { width: 14px; height: 14px; margin-top: 6px; flex: none; }
  .contact-list .indent { padding-left: 23px; }
  .social { position: absolute; left: 165px; top: 351px; display: flex; gap: 12px; }
  .social span { width: 38px; height: 38px; border-radius: 50%; background: var(--social-a); }
  .social span + span { background: var(--social-b); }
  .brand-mark { position: absolute; left: 560px; top: 88px; font-family: "Cinzel", serif; font-weight: 700; font-size: 50px; line-height: 1; color: var(--ink); }
  .expand-btn { position: absolute; left: 707px; top: 164px; width: 58px; height: 58px; border-radius: 50%; background: var(--accent); }

  .about { position: absolute; top: 543px; left: 0; width: 1166px; height: 588px; border-top: 2px solid var(--rule); padding: 43px 144px 0 148px; }
  .about p { font-size: 13px; line-height: 24px; letter-spacing: 0.2px; margin-bottom: 24px; }
  .about p.tight { margin-bottom: 14px; }
  .about p.loose { line-height: 25.5px; margin-bottom: 26px; }
  .about p.spaced { margin-bottom: 49px; }

  .site-footer { position: absolute; top: 1131px; left: 0; width: 1166px; height: 69px; border-top: 2px solid var(--rule); text-align: center; font-size: 9px; line-height: 68px; color: #555; }
</style>
</head>
<body>
<div class="page">
  <nav class="site-nav">
    <ul class="nav-list">
      <li class="nav-item"><svg viewBox="0 0 10 12"><path d="M5 0a4 4 0 0 1 4 4c0 3-4 8-4 8S1 7 1 4a4 4 0 0 1 4-4z" fill="#3c3f41"/></svg>Home</li>
      <li class="nav-item is-active"><svg viewBox="0 0 10 12"><circle cx="5" cy="3" r="2.6" fill="#3c3f41"/><path d="M0 12c0-4 2-5.5 5-5.5S10 8 10 12z" fill="#3c3f41"/></svg>About Me</li>
      <li class="nav-item"><svg viewBox="0 0 12 12"><ellipse cx="6" cy="5" rx="5.3" ry="3.8" fill="none" stroke="#3c3f41" stroke-width="1.3"/><path d="M3 8l-1 3 3-2" fill="#3c3f41"/></svg>Testimonials</li>
      <li class="nav-item"><svg viewBox="0 0 10 12"><rect x="1" y="0.7" width="8" height="10.6" fill="none" stroke="#3c3f41" stroke-width="1.2"/><path d="M3 4h4M3 6h4M3 8h4" stroke="#3c3f41"/></svg>Patient Resources</li>
      <li class="nav-item"><svg viewBox="0 0 12 12"><path d="M2 7V6a4 4 0 0 1 8 0v1" fill="none" stroke="#3c3f41" stroke-width="1.3"/><rect x="1" y="6" width="3" height="4" fill="#3c3f41"/><rect x="8" y="6" width="3" height="4" fill="#3c3f41"/></svg>Contact</li>
    </ul>
    <div class="menu-toggle">MENU<svg width="20" height="12" viewBox="0 0 20 12"><path d="M4 1h16M0 6h20M4 11h16" stroke="#3c3f41" stroke-width="2"/></svg></div>
  </nav>

  <header class="hero">
    <svg class="hero-shape" width="1166" height="474" viewBox="0 0 1166 474">
      <defs>
        <linearGradient id="portrait-tone" x1="0" y1="0" x2="0" y2="1">
          <stop offset="0" stop-color="#e9ebeb"/>
          <stop offset="0.25" stop-color="#c9b3a4"/>
          <stop offset="0.7" stop-color="#c9b3a4"/>
          <stop offset="1" stop-color="#4f6283"/>
        </linearGradient>
      </defs>
      <polygon points="0,0 689,0 808,474 0,474" fill="#a6c9d1"/>
      <path role="img" aria-label="Portrait photograph of the dentist in scrubs" d="M825,474 C790,420 820,340 850,320 C830,260 830,120 900,80 C960,40 1040,60 1060,120 C1080,200 1060,280 1050,320 C1090,340 1160,380 1166,400 L1166,474 Z" fill="url(#portrait-tone)"/>
    </svg>
    <h1 class="hero-name">Doren Kamsel</h1>
    <p class="hero-quals">BDS (Hons) MFDP CDS (Wal)</p>
    <ul class="contact-list">
      <li><svg viewBox="0 0 14 14"><path d="M7 1a4.5 4.5 0 0 1 4.5 4.5C11.5 9 7 13.5 7 13.5S2.5 9 2.5 5.5A4.5 4.5 0 0 1 7 1z" fill="none" stroke="#444" stroke-width="1.2"/><circle cx="7" cy="5.5" r="1.6" fill="#444"/></svg>Glanmorfa Dental Surgery</li>
      <li class="indent">41-43 Ffordd y Bont, Cardiff CF23 9RT.</li>
      <li><svg viewBox="0 0 14 14"><path d="M3 1l3 3-1.5 2a8 8 0 0 0 3.5 3.5L10 8l3 3-2 2C6 13 1 8 1 3z" fill="#444"/></svg>029 2048 3172</li>
      <li><svg viewBox="0 0 14 14"><rect x="1" y="3" width="12" height="8" fill="#444"/><path d="M1 3l6 5 6-5" fill="none" stroke="#a6c9d1" stroke-width="1"/></svg>info@dorenkamsel.com</li>
      <li><svg viewBox="0 0 14 14"><circle cx="7" cy="7" r="5.8" fill="none" stroke="#444" stroke-width="1.1"/><path d="M1.2 7h11.6M7 1.2v11.6M3 3.5h8M3 10.5h8" stroke="#444" stroke-width="0.8"/><ellipse cx="7" cy="7" rx="2.6" ry="5.8" fill="none" stroke="#444" stroke-width="0.8"/></svg>www.dorenkamsel.com</li>
    </ul>
    <div class="social"><span></span><span></span></div>
    <div class="brand-mark">DK</div>
    <div class="expand-btn"><svg width="58" height="58" viewBox="0 0 58 58"><path d="M29 20v18M20 29h18" stroke="#fff" stroke-width="3"/></svg></div>
  </header>

  <main class="about">
    <p>I am a Taff Valley University graduate and registered with the National Dental Register (NDR no. 318572)</p>
    <p>I provide care for my patients at Glanmorfa Dental Surgery, a state of the art private practice in Glanmorfa Village, Cardiff. I have a particular interest in periodontal disease and in restoring missing teeth with dental implants.</p>
    <p class="tight">I work as a Clinical Research Fellow and a Clinical Lecturer at Severnmouth Dental Hospital, University of Severnmouth. My research interests include developing research methodologies, periodontal conditions, bone augmentation and peri-implant lesions, the scientific evaluation of oral health care products, toothwear, dentine hypersensitivity and tooth whitening. I currently partake in clinical research studies with publications in peer reviewed journals. I am involved with undergraduate teaching &amp; training of Periodontology at the University of Severnmouth and I also lecture in the national forum.</p>
    <p class="loose">I am an active member of the Society of Gum Health Practitioners and Global Implant Circle. I am also a Member of the Allied Fellowship of the College of Dental Practitioners (Wales) and the Welsh representative on the committee for the Guild of Implant Dentistry.</p>
    <p class="loose">I enjoy working with my patients in order to meet their oral health requirements and I appreciate that one's experiences and circumstances are fundamental to understanding their dental needs. I therefore believe in a holistic and specific approach tailored to each patient, from the nervous individual to those looking to improve their smile.</p>
    <p>If you would like to find out more about how I could help you, please get in touch.</p>
  </main>

  <footer class="site-footer">Doren Kamsel. Copyright © 2017. All rights reserved.</footer>
</div>
</body>
</html>
```